3 Politically Incorrect Greeting Cards

I would like to see some clean, colorful, and modern designs for 3 "politically incorrect" greeting cards aimed at young, single, successful women. I would like them to say:

Card 1: " Congratulations on not marrying the wrong person"
Card 2: " Congratulations on buying a house without a husband"
Card 3: " Thank you for not forgetting about me now that you have a boyfriend"

My initial thought was to have a white background with simple black writing, but I think a colorful background with a white text box in the middle might be more appropriate. I can't imagine the cards having any images/icons on them, but I'm open to suggestions if you think it would improve on the design. You guys are likely more creative than I am.

I've included a couple pics of looks I like - but like I said - I'm open to suggestions and what I like may not be appropriate for these cards. All the cards can have a similar esthetic or theme (maybe the same fonts but different colors or different color florals in each) or they can be completely different.

Target Market(s)

Young, single, successful women mid-20s to mid 40's.

Font styles to use
Serif
Sans Serif
Other font styles liked:
• Watercolour lettering maybe

Colors

Designer to choose colors to be used in the design.

Requirements
Must have
• Clean, colorful, bright, professional looking. The right tone for the message.
• I think the message is bold so the writing and colors have to be as well. I have included examples of ideas I like.
Nice to have
• Images, illustrations, icons, maybe patterns or some decorative details. Something to make the card more interesting than just the words (like the blue background with black letters one I made). I like a bright pattern with a white box in the center with the text.
Should not have
• Special effects, galaxy pictures, ugly images, bland colors.

```html
<!DOCTYPE html>
<html lang="en">
<head>
<meta charset="utf-8">
<title>Greeting Card Set</title>
<link href="https://fonts.googleapis.com/css2?family=Josefin+Sans:wght@400;700&display=swap" rel="stylesheet">
<style>
  :root {
    --backdrop: #ecebea;
    --ink: #2d2d2d;
    --box-line: #8a8a8a;
    --box-fill: rgba(255, 255, 255, 0.8);
    --rose-soft: #e9c3d2;
    --rose-deep: #b9688f;
    --mint-soft: #cfe9e4;
    --mint-deep: #3fb3a5;
    --sky-soft: #c9e2f3;
    --sky-deep: #5aaee0;
    --accent-rose: #c2407a;
    --accent-teal: #1f9e92;
    --accent-blue: #2f86c4;
  }
  * { margin: 0; padding: 0; box-sizing: border-box; }
  html, body { width: 1200px; height: 914px; overflow: hidden; }
  body {
    background: var(--backdrop);
    position: relative;
    font-family: "Josefin Sans", "Futura", sans-serif;
    color: var(--ink);
  }
  .card {
    position: absolute;
    width: 455px;
    height: 325px;
    background: #fff;
    overflow: hidden;
    box-shadow: 0 3px 10px rgba(0,0,0,0.18);
  }
  .card--married { left: 108px; top: 142px; }
  .card--friend  { left: 665px; top: 142px; }
  .card--house   { left: 385px; top: 531px; }

  .card__pattern { position: absolute; inset: 0; }
  .card--married .card__pattern {
    background: linear-gradient(118deg, var(--rose-soft) 0%, #fff 12%, #fff 40%, var(--rose-soft) 62%, var(--rose-deep) 100%);
  }
  .card--friend .card__pattern {
    background: linear-gradient(118deg, #fff 0%, #fff 35%, var(--mint-soft) 58%, var(--mint-deep) 100%);
  }
  .card--house .card__pattern {
    background: linear-gradient(150deg, var(--sky-deep) 0%, var(--sky-soft) 35%, #f1f4f6 60%, var(--sky-soft) 80%, var(--sky-deep) 100%);
  }

  .card__message {
    position: absolute;
    width: 356px;
    height: 138px;
    border: 1px solid var(--box-line);
    background: var(--box-fill);
    display: flex;
    flex-direction: column;
    justify-content: center;
    align-items: center;
    text-align: center;
    text-transform: uppercase;
    font-weight: 400;
    white-space: nowrap;
    letter-spacing: -0.01em;
  }
  .card--married .card__message { left: 53px; top: 95px; font-size: 24px; line-height: 33px; }
  .card--friend  .card__message { left: 58px; top: 95px; font-size: 18px; line-height: 29px; letter-spacing: -0.02em; }
  .card--house   .card__message { left: 46px; top: 98px; font-size: 23px; line-height: 33.5px; }

  .card__highlight { font-weight: 700; }
  .card--married .card__highlight { color: var(--accent-rose); }
  .card--friend  .card__highlight { color: var(--accent-teal); }
  .card--house   .card__highlight { color: var(--accent-blue); }
</style>
</head>
<body>

  <section class="card card--married">
    <div class="card__pattern" role="img" aria-label="Geometric pattern of overlapping pink, rose and lilac triangles"></div>
    <p class="card__message">
      <span>Congratulations</span>
      <span>On <span class="card__highlight">Not Marrying</span></span>
      <span>The Wrong Person</span>
    </p>
  </section>

  <section class="card card--friend">
    <div class="card__pattern" role="img" aria-label="Geometric pattern of overlapping mint, teal and aqua triangles"></div>
    <p class="card__message">
      <span>Thank You For <span class="card__highlight">Not Forgetting</span></span>
      <span>About Me Now That</span>
      <span>You Have A Boyfriend</span>
    </p>
  </section>

  <section class="card card--house">
    <div class="card__pattern" role="img" aria-label="Geometric pattern of overlapping sky blue, pale grey and sea green triangles"></div>
    <p class="card__message">
      <span>Congratulations On</span>
      <span>Buying A House</span>
      <span><span class="card__highlight">Without</span> A Husband</span>
    </p>
  </section>

</body>
</html>
```